Ad design for a macarons brand

We are a dessert brand with one product line: macarons. Our products delight. Every bite is a dream!

We are launching a new product and would like to lunch a small tactical campaign for the product to boost sales.

The new macron is mango ganache and the middle a mix of sour mango and yuzu (https://www.plumvarell.com/about-the-fruit-584302).

Here are some images we took of the new macaron
https://www.fennlocker.com/sh/qrtwpzhkvbmls/AAFJtRWD-nxPlkhQZ7CeW4DLp?dl=0

I attach the brand guideline document.

Required sizes

1080 x 1350
1080 x 1920

```html
<!DOCTYPE html>
<html lang="en">
<head>
<meta charset="utf-8">
<title>Velles – Mango Yuzu Macaron</title>
<link rel="stylesheet" href="https://fonts.googleapis.com/css2?family=Libre+Caslon+Text:wght@400&family=Figtree:wght@400&display=swap">
<style>
  :root {
    --band-light: #F9CD74;
    --panel-yellow: #F8B531;
    --footer-grey: #A3A3A3;
    --ink-dark: #3D2B0E;
    --ink-body: #54401C;
    --highlight: #FAD68A;
    --logo-black: #06060A;
    --logo-text: #FFFFFF;
  }
  * { margin: 0; padding: 0; box-sizing: border-box; }
  html, body { width: 675px; height: 1200px; overflow: hidden; }
  body { position: relative; background: var(--footer-grey); }

  .hero-photo {
    position: absolute; left: 0; top: 0; width: 675px; height: 418px;
    background:
      radial-gradient(ellipse at 50% 55%, #F0A53A 0%, #E9A045 35%, transparent 70%),
      linear-gradient(180deg, #F2E3B0 0%, #EFC46A 30%, #E9A54A 65%, #EFE6DA 100%);
  }
  .accent-band {
    position: absolute; left: 0; top: 418px; width: 675px; height: 30px;
    background: var(--band-light);
  }
  .message-panel {
    position: absolute; left: 0; top: 448px; width: 675px; height: 469px;
    background: var(--panel-yellow);
  }
  .headline {
    position: absolute; left: 95px; top: 50px;
    font-family: "Libre Caslon Text", serif;
    font-weight: 400; font-size: 55px; line-height: 61px;
    letter-spacing: -2.5px; color: var(--ink-dark);
    text-transform: uppercase;
  }
  .body-copy {
    position: absolute; left: 94px; top: 193px;
    font-family: "Figtree", sans-serif;
    font-size: 30px; line-height: 44px; letter-spacing: -0.6px;
    color: var(--ink-body);
  }
  .body-copy .line { display: block; }
  .body-copy .mark {
    background: linear-gradient(transparent 62%, var(--highlight) 62%, var(--highlight) 95%, transparent 95%);
    padding-right: 8px;
  }
  .cta {
    position: absolute; left: 96px; top: 366px;
    display: flex; align-items: center; gap: 16px;
    font-family: "Libre Caslon Text", serif;
    font-size: 21px; letter-spacing: -1.2px; color: var(--ink-dark);
    text-decoration: none;
  }
  .cta-label { text-decoration: underline; text-underline-offset: 3px; text-decoration-thickness: 1px; }
  .cta svg { width: 10px; height: 14px; }

  .brand-plate {
    position: absolute; left: 205px; top: 985px; width: 266px; height: 134px;
    background: var(--logo-black);
    box-shadow: 0 6px 14px rgba(0,0,0,0.25);
    display: flex; align-items: center; justify-content: center;
  }
  .brand-name {
    font-family: "Libre Caslon Text", serif;
    font-size: 44px; letter-spacing: -1px; color: var(--logo-text);
  }
</style>
</head>
<body>
  <div class="hero-photo" role="img" aria-label="Close-up photo of a pile of mango yuzu macarons with yellow filling on white parchment, mangoes in the background"></div>
  <div class="accent-band"></div>

  <section class="message-panel">
    <h1 class="headline">Velles. Every<br>bite’s a dream.</h1>
    <p class="body-copy">
      <span class="line"><span class="mark">For anyone seeking a</span></span>
      <span class="line"><span class="mark">treat, a gift, or a lift, Velles</span></span>
      <span class="line"><span class="mark">are the perfect product.</span></span>
    </p>
    <a class="cta" href="#">
      <span class="cta-label">TASTE THIS FLAVOR</span>
      <svg viewBox="0 0 10 14" aria-hidden="true"><polyline points="2,1 8,7 2,13" fill="none" stroke="#3D2B0E" stroke-width="1.5"/></svg>
    </a>
  </section>

  <div class="brand-plate">
    <span class="brand-name">VELLES</span>
  </div>
</body>
</html>
```